Decals By Marlo needs a website and logo design

I am starting a home business, "Decals By Marlo", which I will sell car decals/decals of some sort. I am looking for a creative and professional looking website. I do not want anything too plain/bland, or else I could design it myself. I am up for many options, when it comes to text/colors, and I am not opposed to much. Just nothing too plain. Currently have no logo design to use, may also add this to the project as well. ( I use Wordpress for my site server so it has to be compatible to be used with that website.
Also, I make decals that mainly go on car windows, not as big on car body’s. Also put decals on glassware, and other items. But mainly car windows

Industry/Entity Type

Business

Coding

Coded - Design and coding required

Font styles to use
Serif
Sans Serif

Requirements
Nice to have
• some color, not be bland and white everywhere.

```html
<!DOCTYPE html>
<html lang="en">
<head>
<meta charset="utf-8">
<title>Decals By Marlo</title>
<link href="https://fonts.googleapis.com/css2?family=Raleway:wght@400;500;600;700;800;900&display=swap" rel="stylesheet">
<style>
:root{
  --red:#d0161e;
  --red-deep:#a80f15;
  --red-wash:rgba(200,22,30,.82);
  --ink:#1c1c1c;
  --ink-soft:#444;
  --night:#101114;
  --night-2:#1b1d22;
  --paper:#ffffff;
  --mist:#ececec;
  --green:#1f8a5b;
  --muted:#b9b9b9;
}
*{box-sizing:border-box;margin:0;padding:0}
html,body{width:1200px;height:4054px;overflow:hidden}
body{position:relative;background:var(--paper);font-family:"Raleway",sans-serif;color:var(--ink)}
.abs{position:absolute}
.center{left:0;width:1200px;text-align:center}

/* hero */
.hero{position:absolute;left:0;top:0;width:1200px;height:770px;
  clip-path:polygon(0 0,100% 0,100% 680px,50% 770px,0 680px);
  background:radial-gradient(ellipse 520px 300px at 860px 430px,#6d7280 0%,#3a3e48 40%,transparent 75%),
             linear-gradient(180deg,#2a2d34 0%,#15171b 60%,#0d0e11 100%)}
.topbar{top:14px;left:120px;display:flex;gap:26px;font-size:13px;color:#fff;font-weight:600}
.topbar span{display:flex;align-items:center;gap:8px}
.logo{top:46px;left:118px;display:flex;align-items:center;gap:10px}
.logo .mark{width:16px;height:16px;background:var(--red)}
.logo .name{font-size:34px;font-weight:800;color:var(--red);letter-spacing:.5px}
.social{top:12px;left:868px;display:flex;gap:26px}
.social i{display:block;width:16px;height:16px;border-radius:50%;background:#8d8f95}
.nav{top:72px;left:598px;display:flex;gap:32px;font-size:14px;font-weight:600;color:#fff;letter-spacing:.3px}
.search{top:66px;left:1076px}
.chev{top:716px;left:586px}

/* welcome */
.welcome-car{left:150px;top:890px;width:930px;height:380px;border-radius:200px 260px 60px 60px;
  background:radial-gradient(ellipse at 60% 40%,#f4f4f4 0%,#e6e6e6 55%,rgba(255,255,255,0) 80%);opacity:.9}
.welcome-kicker{top:856px;font-size:22px;font-weight:800;letter-spacing:1px}
.welcome-title{top:872px;font-size:88px;font-weight:800;color:var(--red);letter-spacing:2px}
.welcome-sub{top:966px;font-size:28px;font-weight:500;color:var(--ink-soft);letter-spacing:1px}
.welcome-text{top:1024px;left:310px;width:580px;text-align:center;font-size:15px;line-height:21px;color:#333}
.btn-outline{top:1150px;left:454px;width:308px;height:48px;border:2px solid var(--ink);
  font-size:28px;font-weight:500;display:flex;align-items:center;justify-content:center;background:rgba(255,255,255,.6)}

/* services */
.services{left:0;top:1325px;width:1200px;height:648px;
  background:linear-gradient(var(--red-wash),var(--red-wash)),
             radial-gradient(ellipse 600px 260px at 560px 420px,#5a0e10,#2a0608 70%),#3a0709}
.section-title{font-size:36px;font-weight:800;letter-spacing:.5px}
.section-sub{font-size:13px;font-weight:500;letter-spacing:.5px;text-transform:uppercase}
.services .section-title{top:1402px;color:#fff}
.services .section-sub{top:1447px;color:#ffe3e3}
.card{top:1527px;width:256px;height:327px;background:var(--paper);text-align:center;padding-top:52px}
.card h3{font-size:18px;font-weight:700;margin-top:34px;text-transform:uppercase}
.card p{font-size:12px;line-height:16px;color:#333;width:200px;margin:10px auto 0}
.card .more{display:inline-block;margin-top:26px;border:1.5px solid var(--ink);font-size:10px;font-weight:700;padding:4px 10px}

/* gallery */
.gallery{left:0;top:1973px;width:1200px;height:649px;
  background:radial-gradient(ellipse 560px 320px at 600px 300px,#ffffff 0%,#e4e4e4 60%,#d9d9d9 100%)}
.gallery .section-title{top:2048px}
.gallery .section-sub{top:2096px;color:#333}
.tile{width:270px;height:181px;overflow:hidden}
.tile .ph{width:100%;height:100%}
.tile .cap{position:absolute;left:0;bottom:0;width:100%;height:44px;background:rgba(20,20,20,.88);
  color:#fff;font-size:15px;font-weight:500;display:flex;align-items:center;justify-content:center}

/* testimonial */
.testimony{left:0;top:2622px;width:1200px;height:649px;
  background:radial-gradient(ellipse 520px 220px at 740px 300px,#3a3a3a 0%,var(--night-2) 55%,var(--night) 100%)}
.testimony .section-title{top:2696px;color:#fff}
.testimony .section-sub{top:2742px;color:#ddd}
.avatar{top:2811px;left:533px;width:135px;height:135px;border-radius:50%;border:4px solid #fff;background:#9aa0a8}
.person{top:2968px;font-size:14px;font-weight:700;color:#fff}
.role{top:2990px;font-size:13px;color:#ddd}
.quote{top:3050px;left:190px;width:820px;text-align:center;font-size:15px;line-height:25px;color:#eee}
.dots{top:3188px;left:544px;display:flex;gap:20px}
.dots i{width:7px;height:7px;background:var(--red);display:block}

/* map */
.map{left:0;top:3271px;width:1200px;height:446px;
  background:linear-gradient(135deg,#e9e5dc 0%,#dfe7d6 45%,#c9d9ea 100%)}

/* footer */
.footer{left:0;top:3717px;width:1200px;height:337px;
  background:radial-gradient(ellipse 500px 220px at 700px 250px,#3a1a16 0%,#151515 60%,#0b0b0b 100%)}
.footer-cap{left:0;top:3690px;width:1200px;height:40px}
.f-head{font-size:13px;font-weight:700;color:#fff;letter-spacing:.5px}
.f-list{font-size:12px;color:#ddd;line-height:29px;list-style:none}
.f-contact{font-size:12px;color:#ddd}
.f-contact div{display:flex;align-items:flex-start;gap:10px;margin-bottom:14px}
.f-quote{top:3779px;left:630px;width:421px;font-size:11px;line-height:15px;color:#ddd}
.field{height:23px;background:#fff;font-size:10px;color:#777;padding:6px 8px}
.submit{top:3892px;left:911px;width:140px;height:27px;background:var(--red);color:#fff;font-size:13px;font-weight:700;
  display:flex;align-items:center;justify-content:center}
.copyright{top:4028px;font-size:11px;color:#ccc}
</style>
</head>
<body>

<section class="hero" role="img" aria-label="Dark garage photo with a white sports car under spotlights"></section>

<div class="abs topbar">
  <span><svg width="14" height="14" viewBox="0 0 24 24" fill="#fff"><path d="M6.6 10.8a15 15 0 0 0 6.6 6.6l2.2-2.2a1 1 0 0 1 1-.25 11.4 11.4 0 0 0 3.6.57 1 1 0 0 1 1 1V20a1 1 0 0 1-1 1A17 17 0 0 1 3 4a1 1 0 0 1 1-1h3.5a1 1 0 0 1 1 1c0 1.25.2 2.45.57 3.57a1 1 0 0 1-.25 1z"/></svg>(+00) 555 01 234</span>
  <span><svg width="16" height="12" viewBox="0 0 24 18" fill="#fff"><path d="M0 0h24v18H0z"/><path d="M0 0l12 9 12-9" stroke="#222" stroke-width="2" fill="none"/></svg>info@decalsbymarlo.com</span>
</div>

<div class="abs logo"><span class="mark"></span><span class="name">Decals By Marlo</span></div>

<div class="abs social"><i></i><i></i><i></i><i></i><i></i></div>

<nav class="abs nav"><span>HOME</span><span>ABOUT US</span><span>OUR SERVICES</span><span>CONTACT US</span></nav>
<svg class="abs search" width="26" height="26" viewBox="0 0 24 24" fill="none" stroke="#fff" stroke-width="2.4"><circle cx="10" cy="10" r="6.5"/><path d="M15 15l6 6"/></svg>
<svg class="abs chev" width="28" height="20" viewBox="0 0 28 20" fill="none" stroke="#fff" stroke-width="4"><path d="M3 4l11 11L25 4"/></svg>

<!-- welcome -->
<div class="abs welcome-car" role="img" aria-label="Faded white coupe photo behind the welcome text"></div>
<div class="abs center welcome-kicker">WELCOME TO</div>
<div class="abs center welcome-title">DECALS</div>
<div class="abs center welcome-sub">BY MARLO</div>
<p class="abs welcome-text">Lorem ipsum dolor sit amet, consectetur adipiscing elit. Pellentesque eget lacus porta, venenatis erat sit amet, porta lectus. Quisque tincidunt ultrices erat, ac faucibus odio convallis vel. Duis ultricies sem et quam elementum pellentesque. Ut at ante erat. Duis lobortis, tellus vitae rhoncus congue, dui dui tristique arcu, a hendrerit magna mi eu nisi.</p>
<div class="abs btn-outline">see our services &gt;</div>

<!-- services -->
<section class="abs services" role="img" aria-label="Red tinted photo of an orange sports car on a tree lined street"></section>
<h2 class="abs center section-title" style="top:1402px;color:#fff">OUR SERVICES</h2>
<div class="abs center section-sub" style="top:1447px;color:#ffe3e3">We are offering car decals/decals services</div>

<div class="abs card" style="left:168px">
  <svg width="64" height="44" viewBox="0 0 64 44" fill="var(--green)"><path d="M12 4h40l8 18v16h-8v6h-8v-6H20v6h-8v-6H4V22z"/><path d="M16 9h32l5 12H11z" fill="#fff"/><circle cx="14" cy="29" r="4" fill="#fff"/><circle cx="50" cy="29" r="4" fill="#fff"/></svg>
  <h3>Car Decals</h3>
  <p>Lorem ipsum dolor sit amet, consectetur adipiscing elit. Pellentesque eget lacus porta, venenatis erat sit amet, porta lectus.</p>
  <span class="more">READ MORE</span>
</div>
<div class="abs card" style="left:468px">
  <svg width="64" height="44" viewBox="0 0 64 44" fill="var(--green)"><path d="M12 4h40l8 18v16h-8v6h-8v-6H20v6h-8v-6H4V22z"/><path d="M16 9h32l5 12H11z" fill="#fff"/><circle cx="14" cy="29" r="4" fill="#fff"/><circle cx="50" cy="29" r="4" fill="#fff"/></svg>
  <h3>Decals</h3>
  <p>Lorem ipsum dolor sit amet, consectetur adipiscing elit. Pellentesque eget lacus porta, venenatis erat sit amet, porta lectus.</p>
  <span class="more">READ MORE</span>
</div>
<div class="abs card" style="left:768px">
  <svg width="64" height="44" viewBox="0 0 64 44" fill="var(--green)"><path d="M12 4h40l8 18v16h-8v6h-8v-6H20v6h-8v-6H4V22z"/><path d="M16 9h32l5 12H11z" fill="#fff"/><circle cx="14" cy="29" r="4" fill="#fff"/><circle cx="50" cy="29" r="4" fill="#fff"/></svg>
  <h3>Car Wrapping</h3>
  <p>Lorem ipsum dolor sit amet, consectetur adipiscing elit. Pellentesque eget lacus porta, venenatis erat sit amet, porta lectus.</p>
  <span class="more">READ MORE</span>
</div>

<!-- gallery -->
<section class="abs gallery" role="img" aria-label="Light photo of a white car front behind the gallery grid"></section>
<h2 class="abs center section-title" style="top:2048px">OUR LATEST GALLERY</h2>
<div class="abs center section-sub" style="top:2096px;color:#333">See our latest works and products here</div>

<div class="abs tile" style="left:184px;top:2154px"><div class="ph" role="img" aria-label="Yellow sports car with decals" style="background:linear-gradient(160deg,#6f7a4e,#d89a1e 60%,#3b3b2c)"></div><div class="cap">LATEST DECAL DESIGN</div></div>
<div class="abs tile" style="left:461px;top:2154px"><div class="ph" role="img" aria-label="Car covered in sticker bomb decals" style="background:linear-gradient(160deg,#c9c9c9,#8a2226 55%,#e5e5e5)"></div><div class="cap">LATEST DECAL DESIGN</div></div>
<div class="abs tile" style="left:738px;top:2154px"><div class="ph" role="img" aria-label="Yellow hood with black flame decal" style="background:linear-gradient(160deg,#f2ee8a,#d8d24a 60%,#a8a23a)"></div><div class="cap">LATEST DECAL DESIGN</div></div>
<div class="abs tile" style="left:184px;top:2343px"><div class="ph" role="img" aria-label="White hood with black winged decal" style="background:linear-gradient(160deg,#f3f3f3,#bdbdbd 60%,#5a5a5a)"></div><div class="cap">LATEST DECAL DESIGN</div></div>
<div class="abs tile" style="left:461px;top:2343px"><div class="ph" role="img" aria-label="Dark hood with skull decal" style="background:linear-gradient(160deg,#1c1c1c,#5c5c5c 55%,#141414)"></div><div class="cap">LATEST DECAL DESIGN</div></div>
<div class="abs tile" style="left:738px;top:2343px"><div class="ph" role="img" aria-label="Rear window with green villain character decal" style="background:linear-gradient(160deg,#0f2a22,#2f6a4d 55%,#111)"></div><div class="cap">LATEST DECAL DESIGN</div></div>

<!-- testimonial -->
<section class="abs testimony" role="img" aria-label="Dark photo of a car with an orange graphic wrap"></section>
<h2 class="abs center section-title" style="top:2696px;color:#fff">WHAT CUSTOMER SAYS</h2>
<div class="abs center section-sub" style="top:2742px;color:#ddd">Here are some customer testimonials about Decals By Marlo</div>
<div class="abs avatar" role="img" aria-label="Customer portrait photo"></div>
<div class="abs center person">ALEX MORENO</div>
<div class="abs center role">Customer</div>
<p class="abs quote">"Lorem ipsum dolor sit amet, consectetur adipiscing elit. Pellentesque eget lacus porta, venenatis erat sit amet, porta lectus. Quisque tincidunt ultrices erat, ac faucibus odio convallis vel. Duis ultricies sem et quam elementum pellentesque. Ut at ante erat. Duis lobortis, tellus vitae rhoncus congue, dui dui tristique arcu, a hendrerit magna mi eu nisi."</p>
<div class="abs dots"><i></i><i></i><i></i><i></i></div>

<!-- map -->
<section class="abs map" role="img" aria-label="Street map showing the shop location"></section>

<!-- footer -->
<svg class="abs footer-cap" width="1200" height="40" viewBox="0 0 1200 40" preserveAspectRatio="none"><path d="M0 27L1090 27L1120 0L1200 0L1200 40L0 40Z" fill="#141414"/></svg>
<footer class="abs footer" role="img" aria-label="Dark photo of a red car behind the footer"></footer>

<div class="abs f-head" style="top:3745px;left:135px">QUICK LINKS</div>
<ul class="abs f-list" style="top:3776px;left:150px">
  <li>HOME</li><li>ABOUT US</li><li>SERVICES</li><li>LATEST GALLERY</li><li>TESTIMONIALS</li>
</ul>

<div class="abs f-head" style="top:3745px;left:360px">CONTACT US</div>
<div class="abs f-contact" style="top:3780px;left:362px;width:220px">
  <div><svg width="14" height="18" viewBox="0 0 24 30" fill="#fff"><path d="M12 0a10 10 0 0 0-10 10c0 8 10 20 10 20s10-12 10-20A10 10 0 0 0 12 0zm0 14a4 4 0 1 1 0-8 4 4 0 0 1 0 8z"/></svg><span>St. number, places here, barangay city, states</span></div>
  <div><svg width="14" height="14" viewBox="0 0 24 24" fill="#fff"><path d="M6.6 10.8a15 15 0 0 0 6.6 6.6l2.2-2.2a1 1 0 0 1 1-.25 11.4 11.4 0 0 0 3.6.57 1 1 0 0 1 1 1V20a1 1 0 0 1-1 1A17 17 0 0 1 3 4a1 1 0 0 1 1-1h3.5a1 1 0 0 1 1 1c0 1.25.2 2.45.57 3.57a1 1 0 0 1-.25 1z"/></svg><span>(+00) 555 0102 345</span></div>
  <div><svg width="16" height="12" viewBox="0 0 24 18" fill="#fff"><path d="M0 0h24v18H0z"/><path d="M0 0l12 9 12-9" stroke="#222" stroke-width="2" fill="none"/></svg><span>info@decalsbymarlo.com</span></div>
</div>

<div class="abs f-head" style="top:3745px;left:630px">GET A QUOTE</div>
<p class="abs f-quote">Lorem ipsum dolor sit amet, consectetur adipiscing elit. Pellentesque eget lacus porta, venenatis erat sit amet, porta lectus. Quisque tincidunt ultrices erat.</p>
<div class="abs field" style="top:3817px;left:630px;width:202px">NAME</div>
<div class="abs field" style="top:3817px;left:849px;width:202px">PHONE NUMBER</div>
<div class="abs field" style="top:3854px;left:630px;width:202px">EMAIL ADDRESS</div>
<div class="abs submit">SUBMIT</div>

<div class="abs center copyright">Copyright © 2017 Decals by Marlo</div>

</body>
</html>
```